Business card for Chicago based Private Equity Company

We need a business card for our PE company called Crestline Holdings. We want a simple and clean, yet creative card design. The back side should reflect our logo. Also would like to see embossed ideas. Should reflect strength and growth. Our logo is attached. Also need editable file. Details are as follows for Business Card:

Dana Welmore Co-Founder 2750 Marlow Avenue Suite 410 Fernvale, IL 60914 http://www.crestlineholdingsllc.example (D) 630.555.0147 (C) 312.555.0182 (E) dw@crestlineholdingsllc.example

```html
<!DOCTYPE html>
<html lang="en">
<head>
<meta charset="utf-8">
<title>Crestline Holdings – Business Card</title>
<link rel="stylesheet" href="https://fonts.googleapis.com/css2?family=Saira:wght@400;500;600&display=swap">
<style>
  :root {
    --ink: #0b0b0b;
    --steel: #bfbfbf;
    --steel-light: #d6d6d6;
    --steel-dark: #8f8f8f;
    --paper: #ffffff;
    --backdrop: #9c9c9c;
  }
  * { margin: 0; padding: 0; box-sizing: border-box; }
  html, body {
    width: 1200px; height: 895px; overflow: hidden;
    background: var(--backdrop);
    font-family: "Saira", sans-serif;
  }
  .sheet {
    position: relative; width: 1200px; height: 895px;
    display: flex; flex-direction: column; align-items: center;
    justify-content: center; gap: 35px;
  }
  .card {
    position: relative; width: 700px; height: 400px;
    overflow: hidden; box-shadow: 0 6px 18px rgba(0,0,0,.25);
  }
  .card__art { position: absolute; inset: 0; width: 100%; height: 100%; }
  .brand {
    position: absolute; display: flex; align-items: center; gap: 14px;
    color: var(--paper); white-space: nowrap;
  }
  .brand__dot {
    flex: 0 0 auto;
    width: 46px; height: 46px; border-radius: 50%;
    border: 4px solid var(--paper);
  }
  .brand__name {
    font-weight: 500; font-size: 26px; letter-spacing: 3px;
    text-transform: uppercase; line-height: 1;
  }
  .card--front .brand { left: 36px; top: 32px; }
  .card--back .brand { left: 50%; top: 50%; transform: translate(-50%, -50%); }
  .person {
    position: absolute; right: 40px; top: 40px;
    color: var(--paper); white-space: nowrap;
  }
  .person__name { font-size: 21px; font-weight: 500; letter-spacing: 2px; line-height: 1.3; }
  .person__title { font-size: 9px; letter-spacing: 1.5px; margin-top: 2px; text-transform: uppercase; }
  .contact {
    position: absolute; top: 214px; color: var(--paper);
    font-size: 12px; line-height: 24px; letter-spacing: .3px;
    font-style: normal; white-space: nowrap;
  }
  .contact--web { left: 26px; }
  .contact--address { left: 270px; }
  .contact--phone { left: 520px; letter-spacing: 1px; }
</style>
</head>
<body>
<main class="sheet">

  <section class="card card--front" aria-label="Business card front">
    <svg class="card__art" viewBox="0 0 700 400" aria-hidden="true">
      <rect width="700" height="400" fill="var(--ink)"/>
      <rect x="0" y="112" width="700" height="80" fill="var(--steel)"/>
      <polyline points="222,112 244,152 222,192" fill="none" stroke="var(--ink)" stroke-width="5"/>
      <polyline points="230,112 252,152 230,192" fill="none" stroke="var(--steel-dark)" stroke-width="2"/>
      <polyline points="462,112 484,152 462,192" fill="none" stroke="var(--ink)" stroke-width="5"/>
      <polyline points="470,112 492,152 470,192" fill="none" stroke="var(--steel-dark)" stroke-width="2"/>
      <rect x="0" y="345" width="700" height="55" fill="var(--steel)"/>
      <rect x="0" y="352" width="700" height="3" fill="var(--steel-light)"/>
      <g class="icon-globe" fill="none" stroke="var(--paper)" stroke-width="2">
        <circle cx="112" cy="152" r="14"/>
        <ellipse cx="112" cy="152" rx="6" ry="14"/>
        <line x1="98" y1="152" x2="126" y2="152"/>
        <path d="M101 144 H123 M101 160 H123"/>
      </g>
      <g class="icon-pin">
        <path d="M352 136 a11 11 0 0 1 11 11 c0 9 -11 21 -11 21 s-11 -12 -11 -21 a11 11 0 0 1 11 -11 z" fill="var(--paper)"/>
        <circle cx="352" cy="147" r="4" fill="var(--steel)"/>
      </g>
      <g class="icon-phone" fill="none" stroke="var(--paper)" stroke-width="2">
        <rect x="578" y="136" width="18" height="32" rx="3"/>
        <line x1="584" y1="140" x2="590" y2="140"/>
        <circle cx="587" cy="163" r="1.5" fill="var(--paper)"/>
      </g>
    </svg>

    <div class="brand">
      <span class="brand__dot"></span>
      <span class="brand__name">Crestline Holdings</span>
    </div>

    <div class="person">
      <p class="person__name">DANA WELMORE</p>
      <p class="person__title">Co-Founder</p>
    </div>

    <address class="contact contact--web">
      dw@crestlineholdingsllc.example<br>www.crestlineholdingsllc.example
    </address>
    <address class="contact contact--address">
      2750 Marlow Avenue Suite 410<br>Fernvale, IL 60914
    </address>
    <p class="contact contact--phone">(D) 630.555.0147<br>(C) 312.555.0182</p>
  </section>

  <section class="card card--back" aria-label="Business card back">
    <svg class="card__art" viewBox="0 0 700 400" aria-hidden="true">
      <rect width="700" height="400" fill="var(--steel)"/>
      <rect x="0" y="70" width="700" height="260" fill="var(--ink)"/>
      <polyline points="470,0 492,35 470,70" fill="none" stroke="var(--ink)" stroke-width="5"/>
      <polyline points="478,0 500,35 478,70" fill="none" stroke="var(--steel-dark)" stroke-width="2"/>
      <polyline points="210,330 232,365 210,400" fill="none" stroke="var(--ink)" stroke-width="5"/>
      <polyline points="218,330 240,365 218,400" fill="none" stroke="var(--steel-dark)" stroke-width="2"/>
      <polyline points="600,330 622,365 600,400" fill="none" stroke="var(--ink)" stroke-width="5"/>
      <rect x="0" y="392" width="700" height="3" fill="var(--steel-light)"/>
    </svg>

    <div class="brand">
      <span class="brand__dot"></span>
      <span class="brand__name">Crestline Holdings</span>
    </div>
  </section>

</main>
</body>
</html>
```